Velorin business card design

Design a business card for a cryptocurrency company that uses the attached logo. Some example business cards to give you guys a flavor of what we're looking for is given below (of course feel free to be creative):
https://www.plumcardhub.example/studio.aspx?template=4819265_KT3&ag=True&xnav=HSG_Design_Image&rd=1
https://www.plumcardhub.example/studio.aspx?template=3027514_KT3&ag=True&xnav=HSG_Design_Image&rd=1
The business card should be clean/simple and convey the company name, what we're about and the specific persons contact info. In terms of what we're about, we can have our name Velorin, with a line under it that says "Cryptocurrency visualization, analytics, and trading"
We want something futuristic looking but simple / clean.
The color scheme for the logo should be used.
The name of the person and their title should be editable, so we can use the business card design for multiple people.
(Please use the zip file to get the vector graphics and different image formats)

```html
<!DOCTYPE html>
<html lang="en">
<head>
<meta charset="utf-8">
<title>Velorin business card</title>
<link rel="stylesheet" href="https://fonts.googleapis.com/css2?family=Open+Sans:ital,wght@0,400;0,600;0,700;1,400&display=swap">
<style>
  :root {
    --backdrop: #e9e7e3;
    --card-light: #eceef2;
    --card-dark: #0b1b30;
    --ink-navy: #13213a;
    --ink-white: #f2f4f7;
    --ink-muted: #c9d0da;
    --brand-green: #2fae5f;
    --brand-teal: #2a9b8f;
    --brand-blue: #2a6fc0;
    --watermark: #d3dde4;
  }
  * { box-sizing: border-box; margin: 0; padding: 0; }
  html, body {
    width: 1200px;
    height: 800px;
    overflow: hidden;
    background: var(--backdrop);
    font-family: "Open Sans", Arial, sans-serif;
  }
  .canvas {
    position: relative;
    width: 1200px;
    height: 800px;
  }
  .card {
    position: absolute;
    width: 520px;
    height: 300px;
    border-radius: 4px;
    overflow: hidden;
    box-shadow: 0 10px 28px rgba(30, 30, 40, 0.22);
  }

  /* Front */
  .card-front {
    left: 50px;
    top: 150px;
    background: var(--card-light);
  }
  .card-front .watermark {
    position: absolute;
    right: 40px;
    top: -30px;
    width: 230px;
    height: 230px;
  }
  .card-front .brand {
    position: absolute;
    left: 70px;
    top: 122px;
    display: flex;
    align-items: center;
    gap: 22px;
  }
  .brand-square {
    width: 56px;
    height: 56px;
    background: var(--brand-teal);
  }
  .card-front .brand-name {
    font-size: 50px;
    font-weight: 700;
    letter-spacing: 3px;
    color: var(--ink-navy);
    line-height: 1;
  }

  /* Back */
  .card-back {
    left: 630px;
    top: 350px;
    background: var(--card-dark);
    color: var(--ink-white);
  }
  .card-back .mark-decoration {
    position: absolute;
    left: 34px;
    top: 62px;
    width: 176px;
    height: 176px;
  }
  .card-back .brand {
    position: absolute;
    right: 28px;
    top: 38px;
    display: flex;
    align-items: center;
    gap: 10px;
  }
  .card-back .brand-square {
    width: 30px;
    height: 30px;
  }
  .card-back .brand-name {
    font-size: 28px;
    font-weight: 700;
    letter-spacing: 2px;
    color: var(--ink-white);
    line-height: 1;
  }
  .tagline {
    position: absolute;
    right: 28px;
    top: 86px;
    font-size: 12.5px;
    font-style: italic;
    color: var(--ink-muted);
    text-align: right;
    width: 300px;
    line-height: 1.45;
  }
  .person {
    position: absolute;
    right: 28px;
    top: 150px;
    text-align: right;
  }
  .person-name {
    font-size: 20px;
    font-weight: 700;
    letter-spacing: 1px;
    color: var(--brand-green);
    line-height: 1.1;
  }
  .person-title {
    font-size: 13px;
    color: var(--ink-muted);
    margin-top: 2px;
  }
  .contact {
    position: absolute;
    right: 28px;
    bottom: 22px;
    text-align: right;
    font-size: 13px;
    line-height: 1.4;
    color: var(--ink-white);
    list-style: none;
  }
</style>
</head>
<body>
<main class="canvas">

  <section class="card card-front" aria-label="Business card front">
    <svg class="watermark" viewBox="0 0 230 230" role="img" aria-label="Faint brand mark decoration">
      <circle cx="115" cy="115" r="105" fill="none" stroke="var(--watermark)" stroke-width="14"/>
    </svg>
    <div class="brand">
      <span class="brand-square" aria-hidden="true"></span>
      <span class="brand-name">VELORIN</span>
    </div>
  </section>

  <section class="card card-back" aria-label="Business card back">
    <svg class="mark-decoration" viewBox="0 0 176 176" role="img" aria-label="Large brand mark decoration in green to blue">
      <defs>
        <linearGradient id="brandGradient" x1="1" y1="0" x2="0" y2="1">
          <stop offset="0" stop-color="var(--brand-green)"/>
          <stop offset="1" stop-color="var(--brand-blue)"/>
        </linearGradient>
      </defs>
      <circle cx="88" cy="88" r="84" fill="url(#brandGradient)"/>
    </svg>

    <div class="brand">
      <span class="brand-square" aria-hidden="true"></span>
      <span class="brand-name">VELORIN</span>
    </div>

    <p class="tagline">Cryptocurrency visualization, analytics, and trading</p>

    <div class="person">
      <p class="person-name">JOHN DOE</p>
      <p class="person-title">Managing Director</p>
    </div>

    <ul class="contact">
      <li>+12 345 6789</li>
      <li>email@yourdomain.example</li>
      <li>www.yourdomain.example</li>
    </ul>
  </section>

</main>
</body>
</html>
```